Harbor Grace Chapel Stationary and PPT template

Harbor Grace Chapel, an english-speaking church in urban Tokyo, Japan seeks a letterhead, envelope, and powerpoint background to communicate it's brand across all written and digital communications. The successful design should be conservative and classic in keeping with the church's long history as a beacon of light in Tokyo. A branding style guide should be consulted but designs should not emulate the mock design in the guide.

Designs should be classic and in keeping with the logo usage per the style guide. Colours should be faithful to the turquoise of the HGC brand.

The church website can be consulted for more information regarding phone numbers, address, etc.

Paper size- A4
Envelope size- DL
PPT Template- Mostly white background, colours at bottom + logo.

Target Market(s)

Outside vendors, members, prospective members.

Industry/Entity Type

Church

Requirements
Must have
• Church Logo, Address, phone, office email, white background.
Should not have
• contemporary look and feel. Must be classic design

```html
<!DOCTYPE html>
<html lang="en">
<head>
<meta charset="utf-8">
<title>Harbor Grace Chapel Letterhead</title>
<link rel="stylesheet" href="https://fonts.googleapis.com/css2?family=Open+Sans:wght@400;600&family=Gelasio:ital@1&display=swap">
<style>
  :root {
    --teal: #4cc3c4;
    --ink: #2b2b2b;
    --paper: #ffffff;
    --backdrop: #ececea;
  }
  * { box-sizing: border-box; margin: 0; padding: 0; }
  html, body { width: 1200px; height: 1200px; overflow: hidden; }
  body {
    background: var(--backdrop);
    font-family: "Open Sans", Arial, sans-serif;
    color: var(--ink);
    position: relative;
  }
  .sheet {
    position: absolute;
    top: 284px;
    width: 510px;
    height: 721px;
    background: var(--paper);
    box-shadow: 0 2px 10px rgba(0,0,0,0.12);
  }
  .sheet--letter { left: 106px; }
  .sheet--blank { left: 642px; }
  .band-top {
    position: absolute; top: 0; right: 0;
    width: 168px; height: 9px; background: var(--teal);
  }
  .band-bottom {
    position: absolute; bottom: 0; left: 0;
    width: 170px; height: 9px; background: var(--teal);
  }
  .brand { position: absolute; left: 50px; top: 126px; width: 122px; }
  .brand__mark {
    display: flex; align-items: center; gap: 6px;
    color: var(--teal); font-weight: 600; font-size: 9px;
    letter-spacing: 0.07em; text-transform: uppercase; white-space: nowrap;
    padding-bottom: 5px; border-bottom: 1.5px solid var(--teal);
  }
  .brand__square { width: 8px; height: 8px; background: var(--teal); flex: none; }
  .brand__tagline {
    color: var(--teal); font-size: 8.5px; letter-spacing: 0.04em;
    margin-top: 5px; text-align: center; white-space: nowrap;
  }
  .date-field {
    position: absolute; right: 37px; top: 130px; width: 116px;
    border-bottom: 1.5px solid var(--teal); padding-bottom: 6px;
    font-family: "Gelasio", Georgia, serif; font-style: italic;
    font-size: 10px; text-align: right; white-space: nowrap;
  }
  .date-field sup { font-size: 6px; }
  .block { position: absolute; left: 36px; width: 432px; }
  .heading {
    color: var(--teal); font-weight: 400; font-size: 17.5px; line-height: 22px; white-space: nowrap;
  }
  .mission {
    font-family: "Gelasio", Georgia, serif; font-style: italic;
    font-size: 14.5px; line-height: 21px;
  }
  .body-text { font-size: 8.6px; line-height: 17.4px; }
  .beliefs { list-style: none; }
  .beliefs li { font-size: 8.6px; line-height: 14.4px; padding-left: 8px; position: relative; }
  .beliefs li::before {
    content: ""; position: absolute; left: 0; top: 6px;
    width: 3px; height: 3px; background: var(--teal); border-radius: 50%;
  }
  .contact {
    position: absolute; left: 49px; top: 588px;
    font-size: 8.6px; line-height: 10.4px; white-space: nowrap;
  }
  .contact__label { color: var(--teal); font-weight: 600; }
  .contact__lines { margin-bottom: 10px; }
  .contact__key { color: var(--teal); }
  .write-line {
    position: absolute; right: 41px; top: 150px; width: 118px;
    border-bottom: 1.5px solid var(--teal);
  }
</style>
</head>
<body>

<section class="sheet sheet--letter">
  <div class="band-top"></div>
  <div class="brand">
    <div class="brand__mark"><span class="brand__square"></span>Harbor Grace Chapel</div>
    <div class="brand__tagline">Grace for every heart</div>
  </div>
  <div class="date-field">Date:&nbsp; Nov 12<sup>th</sup>, 2017</div>

  <h2 class="block heading" style="top:191px">What We Believe</h2>
  <p class="block mission" style="top:221px">"A welcoming family of faithful, growing believers in the city, carrying the hope of Christ to every neighbour."</p>

  <h2 class="block heading" style="top:284px">Introduction</h2>
  <p class="block body-text" style="top:313px">Harbor Grace Chapel was begun by a small group of families and has grown into an international congregation of English-speaking believers. The word "grace" reminds us that every member comes as a gift, joined from many traditions and countries through one shared trust in the Lord Jesus Christ. The people of Harbor Grace Chapel bring their own stories of faith into worship, friendship, and care for the city. Harbor Grace Chapel is self-governing and supported by its members.</p>

  <h2 class="block heading" style="top:419px">What characterizes our church</h2>
  <p class="block body-text" style="top:447px">The people of Harbor Grace Chapel are called to share the good news of God's love in Jesus Christ our Lord through lives of faithful service:</p>
  <ul class="block beliefs" style="top:491px">
    <li>we gather to worship the one, true and living God;</li>
    <li>we proclaim Christ and the hope He brings to all people;</li>
    <li>and led by the Holy Spirit we grow together and care for one another in a fellowship of love and prayer.</li>
  </ul>

  <div class="contact">
    <div class="contact__label">Visit Us:</div>
    <div class="contact__lines">Harbor Grace Chapel,<br>3-12-4 Minato Garden, Minato-ku,<br>Tokyo 105-0022</div>
    <div><span class="contact__key">T:</span> +81 3-5550-0182</div>
    <div><span class="contact__key">F:</span> +81 3-5550-0194</div>
    <div><span class="contact__key">E:</span> office@harborgracechapel.org</div>
  </div>
  <div class="band-bottom"></div>
</section>

<section class="sheet sheet--blank">
  <div class="band-top"></div>
  <div class="brand">
    <div class="brand__mark"><span class="brand__square"></span>Harbor Grace Chapel</div>
    <div class="brand__tagline">Grace for every heart</div>
  </div>
  <div class="write-line"></div>
  <div class="contact">
    <div class="contact__label">Visit Us:</div>
    <div class="contact__lines">Harbor Grace Chapel,<br>3-12-4 Minato Garden, Minato-ku,<br>Tokyo 105-0022</div>
    <div><span class="contact__key">T:</span> +81 3-5550-0182</div>
    <div><span class="contact__key">F:</span> +81 3-5550-0194</div>
    <div><span class="contact__key">E:</span> office@harborgracechapel.org</div>
  </div>
  <div class="band-bottom"></div>
</section>

</body>
</html>
```